Sale of South Sea and Tahitian Pearl Jewellery, online business

I need a business card designed for my website business. We sell South Sea and Tahitian Pearl Jewellery. The colour theme for the website is black and white and would like to carry this through to business cards. Our brand is very elegant and stylish, would like sketch picture of women or fashion involving pearls if not the sketched picture then have the card very plan. below are pictures of the ideas I like and also the logo and writing that is used on my jewellery boxes.
Font is English Hand DB

Target Market(s)

30 and over women in the high end of the market

Industry/Entity Type

Business

Contact Information for Business Card

Business name - Varno Gems( front of card)
Back of card -Details
Rosalind Thackery
Gemmologist MDRS
email: rosalind@varnogems.com.au
website: varnogems.com.au
mob: +61 427 508 193
Perth Australia

Varno Stelle PTY T/AS Varno Gems
ABN 47 283 915 604

Colors
1b1b1b
ffffff
85cae6

Requirements
Must have
• Black and white colour preferably black card with white writing and picture.
• The Same writing as logo and writing on box packaging, attached a file with writing.
• Business name on one side of the card and all other details on the other side.
• Can have tiny hints of the harbour blue colour.
• Font: English Hand DB
Nice to have
• I really like the idea of having a sketch of a stylish or elegent lady wearing pearls or a sketch of a pearl, if not the sketch a really plain and simple card.
Should not have
• busy patterns.

```html
<!DOCTYPE html>
<html lang="en">
<head>
<meta charset="utf-8">
<title>Varno Gems – Business Card</title>
<link href="https://fonts.googleapis.com/css2?family=Montserrat:wght@400;600&display=swap" rel="stylesheet">
<style>
  :root {
    --backdrop: #e9e6e1;
    --card: #0e0e0e;
    --card-edge: #1b1b1b;
    --ink: #ffffff;
    --ink-soft: #d9d9d9;
    --rule: #8a8a8a;
  }
  * { margin: 0; padding: 0; box-sizing: border-box; }
  html, body { width: 1200px; height: 913px; overflow: hidden; }
  body {
    background: var(--backdrop);
    font-family: "Montserrat", Arial, sans-serif;
    color: var(--ink);
    position: relative;
  }
  .card {
    position: absolute;
    width: 540px;
    height: 310px;
    border-radius: 16px;
    background: linear-gradient(135deg, var(--card-edge) 0%, var(--card) 55%, #050505 100%);
    box-shadow: 0 18px 36px rgba(0,0,0,0.28);
    overflow: hidden;
  }
  .card--details { left: 70px; top: 140px; }
  .card--brand { left: 590px; top: 465px; }

  /* details side */
  .brand-mark {
    position: absolute;
    left: 40px; top: 128px;
    display: flex; align-items: center; gap: 12px;
  }
  .brand-mark__dot {
    width: 22px; height: 22px;
    border: 1.5px solid var(--ink);
    border-radius: 50%;
  }
  .brand-mark__name {
    font-size: 22px; font-weight: 400; letter-spacing: 0.5px;
  }
  .divider {
    position: absolute;
    left: 232px; top: 60px;
    width: 1px; height: 120px;
    background: linear-gradient(to bottom, rgba(255,255,255,0), var(--rule) 40%, var(--ink) 100%);
  }
  .contact {
    position: absolute;
    left: 262px; top: 52px;
    line-height: 1.35;
  }
  .contact__name { font-size: 20px; font-weight: 600; }
  .contact__title { font-size: 13px; color: var(--ink-soft); }
  .contact__city { font-size: 13px; color: var(--ink-soft); margin: 12px 0 8px; }
  .contact__list { list-style: none; font-size: 13px; }
  .contact__list li { display: flex; align-items: center; gap: 8px; margin-bottom: 2px; }
  .contact__list svg { width: 11px; height: 11px; flex: none; }

  /* brand side */
  .brand-name {
    position: absolute;
    left: 0; right: 0; top: 96px;
    text-align: center;
    font-size: 50px; font-weight: 400; letter-spacing: 1px;
  }
  .legal {
    position: absolute;
    left: 0; right: 0; top: 196px;
    text-align: center;
    font-size: 13px; line-height: 1.5; color: var(--ink-soft); letter-spacing: 0.4px;
  }
</style>
</head>
<body>
  <section class="card card--details">
    <div class="brand-mark">
      <span class="brand-mark__dot"></span>
      <span class="brand-mark__name">Varno Gems</span>
    </div>
    <div class="divider"></div>
    <div class="contact">
      <p class="contact__name">Rosalind Thackery</p>
      <p class="contact__title">Gemmologist MDRS</p>
      <p class="contact__city">Perth Australia</p>
      <ul class="contact__list">
        <li>
          <svg viewBox="0 0 12 12" fill="none" stroke="#fff" stroke-width="1.2"><rect x="3" y="0.8" width="6" height="10.4" rx="1"/><line x1="5" y1="9.3" x2="7" y2="9.3"/></svg>
          +61 427 508 193
        </li>
        <li>
          <svg viewBox="0 0 12 12" fill="none" stroke="#fff" stroke-width="1.2"><rect x="0.8" y="2.2" width="10.4" height="7.6" rx="0.8"/><polyline points="1,2.6 6,6.6 11,2.6"/></svg>
          rosalind@varnogems.com.au
        </li>
        <li>
          <svg viewBox="0 0 12 12" fill="none" stroke="#fff" stroke-width="1.1"><circle cx="6" cy="6" r="5"/><ellipse cx="6" cy="6" rx="2.2" ry="5"/><line x1="1" y1="6" x2="11" y2="6"/></svg>
          www.varnogems.com.au
        </li>
      </ul>
    </div>
  </section>

  <section class="card card--brand">
    <h1 class="brand-name">Varno Gems</h1>
    <p class="legal">Varno Stelle PTY T/AS Varno Gems<br>ABN 47 283 915 604</p>
  </section>
</body>
</html>
```